3 JPG Website Page Mockups need tidying / made into layered PSDs

Our website is aimed at creating a financial eduction site for females.

We have mockups of each page which are provided in jpeg.... but they need to be tidied up, layered into PSD (with descriptive layer names to allow coding from and no flattening - each object needs it's own layer) and we welcome any creative improvements suggested (although we are pretty happy with the way it's laid out at the moment as it is), without changing the feel, colour scheme or functionality of the site.

Three pages are needed:
Home page when not logged in
Home page when logged in
Topic header page

Please just upload the homepage to bid for the job... the winning designer will then have 5 days after they've been chosen to supply the psds of the other 2 pages .

I have also uploaded an image that can be used as a placeholder in the top box.
Thanks

As requested... Current font is Gill Sans MT

Thanks

Hi
Thanks for your designs.... For those of you still using the 4 circles (which I quite like), but haven't yet done so, could you see if you can move them around slightly to that the words don't get covered by the next circle?

Thanks

Reason: Designe has asked for An extension to work on new icons... would like to give them the time to see what they come up with, thanks

Industry/Entity Type

Financial

Requirements
Must have
• Maintain current feel & colour scheme of the website

```html
<!DOCTYPE html>
<html lang="en">
<head>
<meta charset="utf-8">
<title>Purse &amp; Prosper — Home</title>
<link href="https://fonts.googleapis.com/css2?family=PT+Serif:wght@400;700&family=Arimo:wght@400;700&display=swap" rel="stylesheet">
<style>
  :root {
    --navy: #0c3a5c;
    --navy-deep: #07243b;
    --navy-top: #0a1a2a;
    --accent: #f07b1f;
    --text: #0d3a5e;
    --muted: #7d7d7d;
    --grey-head: #a9a9a9;
    --line: #d8d8d8;
    --panel: #ffffff;
    --btn-light: #e9eef3;
  }
  * { margin: 0; padding: 0; box-sizing: border-box; }
  html, body { width: 1197px; height: 1200px; overflow: hidden; }
  body {
    position: relative;
    background: #fff;
    font-family: "Arimo", Arial, sans-serif;
    color: var(--text);
  }
  h1, h2, h3 { font-weight: 400; }
  .top-band {
    position: absolute; left: 0; top: 0; width: 1197px; height: 289px;
    background: linear-gradient(180deg, var(--navy-top) 0%, #0c2f4c 55%, #0f446a 100%);
  }

  /* Main navigation */
  .main-nav {
    position: absolute; left: 170px; top: 33px; height: 31px;
    display: flex; align-items: center;
  }
  .home-tab {
    width: 41px; height: 31px; background: var(--navy);
    border-radius: 5px 5px 0 0; display: flex; align-items: center; justify-content: center;
  }
  .main-nav a {
    font-family: "PT Serif", Georgia, serif; font-size: 18px; color: #7f95a8;
    text-decoration: none; padding: 0 13px; border-right: 2px dotted #5d7186; line-height: 20px;
  }
  .main-nav a:last-child { border-right: none; }

  /* Header panel */
  .header-panel {
    position: absolute; left: 170px; top: 64px; width: 857px; height: 116px;
    background: var(--navy); border-radius: 0 4px 0 0;
  }
  .brand {
    position: absolute; left: 32px; top: 24px; width: 180px;
    font-family: "PT Serif", Georgia, serif; color: #fff; font-size: 31px; line-height: 32px;
  }
  .divider-v { position: absolute; top: 26px; height: 60px; border-left: 2px dotted #6f89a1; }
  .search-label { position: absolute; left: 233px; top: 12px; font-family: "PT Serif", Georgia, serif; font-size: 15px; color: #fff; }
  .search-box {
    position: absolute; left: 233px; top: 36px; width: 360px; height: 26px;
    background: #fff; border-radius: 3px; border: 1px solid #c9d3dc;
    font-size: 13px; color: #9aa4ad; padding: 5px 9px;
  }
  .search-box svg { position: absolute; right: 9px; top: 5px; }
  .quick-links { position: absolute; left: 234px; top: 70px; display: flex; gap: 30px; }
  .quick-links span {
    font-family: "PT Serif", Georgia, serif; font-size: 13px; color: #e6edf3; text-align: center;
    display: flex; flex-direction: column; align-items: center; white-space: nowrap;
  }
  .quick-links span::after { content: "»"; transform: rotate(90deg); font-size: 11px; margin-top: 2px; color: #cfdbe6; }
  .header-btn {
    position: absolute; top: 44px; height: 24px; padding: 0 8px; white-space: nowrap;
    background: var(--btn-light); border: 1px solid #fff; border-radius: 3px;
    font-family: "PT Serif", Georgia, serif; font-size: 13px; color: var(--text); line-height: 22px;
  }

  /* Welcome bar */
  .welcome-bar {
    position: absolute; left: 180px; top: 177px; width: 837px; height: 28px; background: #fff;
    border: 1px solid var(--line); box-shadow: 0 4px 6px rgba(0,0,0,.12);
    display: flex; align-items: center; padding: 0 9px; z-index: 3; white-space: nowrap;
  }
  .welcome-bar .greeting { font-family: "PT Serif", Georgia, serif; font-size: 16px; color: #111; }
  .welcome-bar .member { margin-left: auto; font-size: 12px; color: #222; }
  .welcome-bar .auth { display: flex; align-items: center; gap: 4px; font-size: 12px; font-weight: 700; color: #111; margin-left: 29px; }
  .sq { width: 14px; height: 14px; background: var(--accent); display: inline-block; }

  /* Hero */
  .hero {
    position: absolute; left: 170px; top: 180px; width: 857px; height: 291px;
    background: #fff; border: 1px solid var(--line); border-radius: 0 0 5px 5px; overflow: hidden;
  }
  .hero-art {
    position: absolute; right: 0; top: 0; width: 530px; height: 291px;
    background: linear-gradient(100deg, rgba(255,255,255,1) 0%, #e8ecef 35%, #cdd6dc 60%, #eef2f5 100%);
  }
  .hero-title {
    position: absolute; left: 74px; top: 92px; width: 400px;
    font-family: "PT Serif", Georgia, serif; font-size: 25px; line-height: 28px; color: #111;
  }
  .hero-title em { font-style: normal; color: var(--accent); }
  .btn-primary {
    position: absolute; height: 30px; padding: 0 10px; white-space: nowrap;
    background: linear-gradient(180deg, #1b557f, #0b3556); border-radius: 4px;
    box-shadow: 0 2px 3px rgba(0,0,0,.35); color: #fff;
    font-family: "PT Serif", Georgia, serif; font-size: 15px; line-height: 30px;
  }
  .dots { position: absolute; left: 74px; top: 254px; display: flex; gap: 7px; }
  .dots i { width: 12px; height: 12px; border-radius: 50%; border: 1px solid #bbb; display: block; }
  .dots i.on { background: var(--navy); border: 2px solid #cfd8df; }
  .arrow { position: absolute; top: 132px; }

  /* Topic panel */
  .panel { position: absolute; background: var(--panel); border: 1px solid var(--line); border-radius: 5px; }
  .topic { left: 170px; top: 481px; width: 857px; height: 294px; overflow: hidden; }
  .video {
    position: absolute; left: 30px; top: 30px; width: 310px; height: 237px;
    background: #111; border: 2px solid #111;
  }
  .video-frame { position: absolute; left: 0; top: 0; width: 306px; height: 215px;
    background: linear-gradient(135deg, #c9c3bd, #f0e8e3 45%, #8a8d95 100%); }
  .video-bar { position: absolute; left: 0; bottom: 0; width: 306px; height: 18px; background: #1a1a1a; }
  .topic-title { position: absolute; left: 366px; top: 38px; font-family: "PT Serif", Georgia, serif; font-size: 26px; color: var(--text); white-space: nowrap; }
  .topic-sub { position: absolute; left: 366px; top: 68px; width: 440px; font-family: "PT Serif", Georgia, serif; font-weight: 700; font-size: 25px; line-height: 28px; color: var(--grey-head); }
  .steps-art {
    position: absolute; left: 385px; top: 130px; width: 472px; height: 164px;
    background: linear-gradient(160deg, rgba(255,255,255,0) 0%, #e8f2f8 45%, #cfe6f3 100%);
  }
  .step-label { position: absolute; font-family: "PT Serif", Georgia, serif; font-size: 13px; line-height: 14px; color: var(--text); text-align: center; font-weight: 700; white-space: nowrap; }

  /* Content boxes */
  .box-left { left: 170px; top: 784px; width: 423px; height: 223px; }
  .box-right { left: 604px; top: 784px; width: 423px; height: 223px; }
  .box-title { position: absolute; left: 17px; top: 20px; font-family: "PT Serif", Georgia, serif; font-size: 22px; color: var(--text); white-space: nowrap; }
  .box-copy { position: absolute; left: 17px; top: 60px; width: 390px; font-size: 12px; line-height: 15px; color: var(--muted); }
  .box-link { position: absolute; left: 17px; top: 180px; font-family: "PT Serif", Georgia, serif; font-size: 15px; color: var(--text); }
  .articles { position: absolute; left: 19px; top: 56px; list-style: none; }
  .articles li { display: flex; align-items: center; gap: 10px; height: 29.5px; font-size: 12.5px; color: var(--muted); white-space: nowrap; }

  /* Icon row */
  .icon-item {
    position: absolute; top: 1033px; transform: translateX(-50%);
    display: flex; flex-direction: column; align-items: center; white-space: nowrap;
    font-family: "PT Serif", Georgia, serif; font-size: 15px; line-height: 20px; color: var(--text);
  }
  .icon-art { width: 52px; height: 52px; border-radius: 10px; margin-bottom: 14px; }
  .footer { position: absolute; left: 170px; top: 1134px; width: 857px; border-top: 1px solid var(--navy); padding: 10px 9px 0; display: flex; justify-content: space-between; font-size: 12px; color: var(--text); }
</style>
</head>
<body>
  <div class="top-band"></div>

  <nav class="main-nav">
    <div class="home-tab">
      <svg width="20" height="18" viewBox="0 0 20 18"><path d="M10 1 L19 9 H16 V17 H12 V12 H8 V17 H4 V9 H1 Z" fill="#fff"/></svg>
    </div>
    <a>Polls</a><a>Events</a><a>Learning Centre</a><a>Find an Adviser</a><a>Ask a Question</a><a>About us</a>
  </nav>

  <header class="header-panel">
    <div class="brand">Purse &amp;<br>Prosper</div>
    <div class="divider-v" style="left:219px"></div>
    <div class="search-label">What are you looking for?</div>
    <div class="search-box">Search Purse &amp; Prosper for...
      <svg width="18" height="16" viewBox="0 0 18 16"><circle cx="7" cy="6.5" r="5" fill="none" stroke="#888" stroke-width="2"/><path d="M11 10 L16 14.5" stroke="#888" stroke-width="3"/></svg>
    </div>
    <div class="quick-links"><span>Popular</span><span>Explore the Learning Centre</span><span>Ask a Question</span></div>
    <div class="divider-v" style="left:611px"></div>
    <div class="header-btn" style="left:628px">» Find an Advise</div>
    <div class="header-btn" style="left:747px">» Contact us</div>
  </header>

  <section class="hero">
    <div class="hero-art" role="img" aria-label="Stopwatch resting on a rising financial chart"></div>
    <svg class="arrow" style="left:18px" width="20" height="28" viewBox="0 0 20 28"><path d="M16 3 L5 14 L16 25" fill="none" stroke="var(--navy)" stroke-width="4"/></svg>
    <svg class="arrow" style="left:818px" width="20" height="28" viewBox="0 0 20 28"><path d="M4 3 L15 14 L4 25" fill="none" stroke="var(--navy)" stroke-width="4"/></svg>
    <h1 class="hero-title">We’re Building World biggest community Dedicated to the <em>Purse&amp;Prosper</em> of Women.</h1>
    <div class="btn-primary" style="left:74px;top:193px">» join now for FREE</div>
    <div class="dots"><i></i><i class="on"></i><i></i></div>
  </section>

  <div class="welcome-bar">
    <span class="greeting">Welcome to the new <b>Purse&amp;Prosper.</b></span>
    <span class="member">Already a member?</span>
    <span class="auth"><i class="sq"></i>Login</span>
    <span class="auth"><i class="sq"></i>Forgotten Password</span>
  </div>

  <section class="panel topic">
    <div class="video">
      <div class="video-frame" role="img" aria-label="Video still of three colleagues reviewing finances at a laptop"></div>
      <svg style="position:absolute;left:124px;top:66px" width="66" height="86" viewBox="0 0 66 86"><path d="M2 2 L64 43 L2 84 Z" fill="#111"/></svg>
      <div class="video-bar">
        <svg width="306" height="18"><path d="M10 5 L16 9 L10 13 Z" fill="#fff"/><rect x="28" y="8" width="240" height="2" fill="#555"/><rect x="272" y="7" width="26" height="4" fill="#2c6fb0"/></svg>
      </div>
    </div>
    <h2 class="topic-title">July Topic : Preparing for Retirement</h2>
    <div class="topic-sub">Tomorrow Can Belong to Those Whos Prepare Today.</div>
    <div class="steps-art" role="img" aria-label="Figures climbing a staircase chart of retirement steps"></div>
    <div class="btn-primary" style="left:366px;top:159px">» learn more</div>
    <div class="step-label" style="left:540px;top:134px">5 Minute<br>Guide<br>PDF</div>
    <div class="step-label" style="left:604px;top:200px">Take Our Poll<br>Vote</div>
    <div class="step-label" style="left:711px;top:242px">Real Women<br>Real Storis<br>See Video</div>
  </section>

  <section class="panel box-left">
    <h3 class="box-title">Catch up with our latest Newsletter</h3>
    <p class="box-copy">Lorem Ipsum is simply dummy text of the printing and typesetting industry. Lorem Ipsum has been the industry's standard dummy text ever since the 1500s, when an unknown printer took a galley of type and scrambled it to make a type specimen book. It has survived not only five centuries, but also the leap into electronic typesetting, remaining essentially unchanged.</p>
    <div class="box-link">» See the Newsletter NOW</div>
  </section>

  <section class="panel box-right">
    <h3 class="box-title">Latest Articles of Interest</h3>
    <ul class="articles">
      <li><svg width="20" height="18" viewBox="0 0 20 18"><path d="M10 1 L19 9 H16 V17 H4 V9 H1 Z" fill="#c8643a"/></svg>What is the real cost of having a bady</li>
      <li><svg width="20" height="18" viewBox="0 0 20 18"><path d="M1 16 L7 9 L11 12 L18 3" fill="none" stroke="#d22" stroke-width="2.5"/><rect x="1" y="16" width="18" height="2" fill="#2a8a3a"/></svg>Understanding the Risk and Returm of different asset types</li>
      <li><svg width="20" height="18" viewBox="0 0 20 18"><circle cx="9" cy="9" r="7.5" fill="#e6f0f8" stroke="#3f79a8" stroke-width="1.5"/><path d="M9 4 V9 L12 11" stroke="#3f79a8" stroke-width="1.5" fill="none"/></svg>How much do I need to Retire?</li>
      <li><svg width="20" height="18" viewBox="0 0 20 18"><path d="M1 16 L7 9 L11 12 L18 3" fill="none" stroke="#d22" stroke-width="2.5"/><rect x="1" y="16" width="18" height="2" fill="#2a8a3a"/></svg>Interest Rates and you</li>
    </ul>
  </section>

  <div class="icon-item" style="left:236px"><div class="icon-art" role="img" aria-label="Shirt and tie icon" style="background:linear-gradient(#f4f4f4,#c9c9c9)"></div>Welcome</div>
  <div class="icon-item" style="left:318px"><div class="icon-art" role="img" aria-label="Calendar icon" style="background:linear-gradient(#5b8fc4,#e8e8e8)"></div>Events</div>
  <div class="icon-item" style="left:401px"><div class="icon-art" role="img" aria-label="Film reel icon" style="background:linear-gradient(#9aa0a6,#4d5257)"></div>Webcasts</div>
  <div class="icon-item" style="left:494px"><div class="icon-art" role="img" aria-label="House icon" style="background:linear-gradient(#c06a3a,#e9d7b8)"></div>My family</div>
  <div class="icon-item" style="left:609px"><div class="icon-art" role="img" aria-label="Rising bar chart icon" style="background:linear-gradient(#e6e6e6,#d94a2a)"></div>My Investments</div>
  <div class="icon-item" style="left:739px"><div class="icon-art" role="img" aria-label="Clock and calendar icon" style="background:linear-gradient(#cfe1f0,#7ea9cc)"></div>My Retirement</div>
  <div class="icon-item" style="left:850px"><div class="icon-art" role="img" aria-label="Handshake icon" style="background:linear-gradient(#e9c9a6,#8aa5c2)"></div>My Estate</div>
  <div class="icon-item" style="left:951px"><div class="icon-art" role="img" aria-label="Meditation figure icon" style="background:radial-gradient(#6cc24a,#2f8a2a);border-radius:50%"></div>My lifestyes</div>

  <footer class="footer">
    <span>Copyright © 2000-2013 Purse &amp; Prosper.</span>
    <span>All rights reserved.</span>
  </footer>
</body>
</html>
```